Reid Calloway Fitness Business Card

I Need a really cool and creative yet modern and cutting edge. I run a personal training company, I have a logo already which ill submit images of. Id like the base colors to be black and white with a little red as a highlight color. Charcoal grey is fine also. My clientele is mostly comprised of young professionals who are in touch with modern culture art and are interested in "cool" so if there was one thing i want this business card to be it sexy and cool.

Target Market(s)

young professionals who are image conscious, care about their health, looking and feeling good. They know what is cool and expect the best.

Industry/Entity Type

Training

Requirements
Must have
• - must be a 2 sided card
- must include the following:

Reid Calloway CPT
604 392 7715
Reid@ReidCallowayFitness.example
www.ReidCallowayFitness.example
Nice to have
• id like to see some unconventional shape ideas as well as conventional ones

```html
<!DOCTYPE html>
<html lang="en">
<head>
<meta charset="utf-8">
<title>Reid Calloway Fitness — Business Card</title>
<link rel="stylesheet" href="https://fonts.googleapis.com/css2?family=Didact+Gothic&display=swap">
<style>
  :root {
    --backdrop: #e4e5e7;
    --brand-red: #e3141b;
    --ink: #111111;
    --paper: #ffffff;
    --charcoal: #0c0c0c;
  }
  html, body {
    margin: 0;
    padding: 0;
    width: 857px;
    height: 1200px;
    overflow: hidden;
    background: var(--backdrop);
  }
  .sheet {
    position: relative;
    width: 857px;
    height: 1200px;
  }
  .card {
    position: absolute;
    left: 78px;
    width: 700px;
    height: 400px;
    filter: drop-shadow(0 6px 10px rgba(0,0,0,0.25));
  }
  .card--front { top: 130px; }
  .card--back { top: 670px; }
  .card svg { display: block; width: 700px; height: 400px; }
  .card-frame { fill: var(--brand-red); }
  .card-panel--front { fill: var(--paper); }
  .card-panel--back { fill: var(--charcoal); }
  .type {
    font-family: "Didact Gothic", "Century Gothic", sans-serif;
  }
  .brand-name { font-size: 36px; }
  .brand-name--back { font-size: 30px; }
  .brand-name--dark { fill: var(--ink); }
  .brand-name--light { fill: var(--paper); }
  .brand-dot { fill: var(--brand-red); }
  .tagline { font-size: 19px; font-style: italic; }
  .tagline--dark { fill: var(--ink); }
  .tagline--light { fill: var(--paper); }
  .tagline-lead { fill: var(--brand-red); }
  .contact-line { fill: var(--paper); font-size: 22px; }
  .contact-icon { fill: var(--brand-red); stroke: var(--paper); stroke-width: 2; }
  .contact-glyph { fill: var(--paper); font-size: 15px; }
  .contact-glyph--small { font-size: 9px; }
  .phone-glyph { fill: none; stroke: var(--paper); stroke-width: 2.4; stroke-linecap: round; }
</style>
</head>
<body>
<main class="sheet">

  <section class="card card--front" aria-label="Business card front">
    <svg viewBox="0 0 700 400" xmlns="http://www.w3.org/2000/svg">
      <path class="card-frame" d="M0 0 H670 Q700 0 700 30 V400 H110 Q0 400 0 290 Z"/>
      <path class="card-panel--front" d="M22 22 H648 Q678 22 678 52 V354 H140 Q22 354 22 236 Z"/>
      <g class="type">
        <circle class="brand-dot" cx="190" cy="194" r="12"/>
        <text class="brand-name brand-name--dark" x="216" y="206">Reid Calloway Fitness</text>
        <text class="tagline tagline--dark" x="560" y="240" text-anchor="end"><tspan class="tagline-lead">Built</tspan>...Better</text>
      </g>
    </svg>
  </section>

  <section class="card card--back" aria-label="Business card back">
    <svg viewBox="0 0 700 400" xmlns="http://www.w3.org/2000/svg">
      <path class="card-frame" d="M0 0 H670 Q700 0 700 30 V400 H110 Q0 400 0 290 Z"/>
      <path class="card-panel--back" d="M22 22 H648 Q678 22 678 52 V354 H140 Q22 354 22 236 Z"/>
      <g class="type">
        <circle class="brand-dot" cx="68" cy="92" r="10"/>
        <text class="brand-name brand-name--light brand-name--back" x="90" y="104">Reid Calloway Fitness</text>
        <text class="tagline tagline--light" x="640" y="148" text-anchor="end"><tspan class="tagline-lead">Built</tspan>...Better</text>

        <text class="contact-line" x="600" y="198" text-anchor="end">Reid Calloway NQFA CPT</text>

        <text class="contact-line" x="600" y="242" text-anchor="end">604 392 7715</text>
        <circle class="contact-icon" cx="630" cy="235" r="13"/>
        <path class="phone-glyph" d="M624 228 Q622 236 630 243 Q634 245 637 242"/>

        <text class="contact-line" x="600" y="284" text-anchor="end">Reid@ReidCallowayFitness.example</text>
        <circle class="contact-icon" cx="630" cy="277" r="13"/>
        <text class="contact-glyph" x="630" y="282" text-anchor="middle">@</text>

        <text class="contact-line" x="600" y="326" text-anchor="end">www.ReidCallowayFitness.example</text>
        <circle class="contact-icon" cx="630" cy="319" r="13"/>
        <text class="contact-glyph contact-glyph--small" x="630" y="322" text-anchor="middle">www</text>
      </g>
    </svg>
  </section>

</main>
</body>
</html>
```